Jolly Paws Business Card Update

I have a business card which I love. I want to keep the same logo, colours, font and style. I want to upgrade the scripting and remove some elements and add others.
On the front side under Services - remove the existing wording and insert - Providing individual coaching strategies to create happy, healthy and social canine companions
Under Rebecca Thornbury amend the current wording to read: Qualified in Dog Behavioural Training, Natural Animal Healthcare and Animal Health Science
On the reverse side to remove the web address.

```html
<!DOCTYPE html>
<html lang="en">
<head>
<meta charset="utf-8">
<title>Jolly Paws Business Card</title>
<link href="https://fonts.googleapis.com/css2?family=Ubuntu:wght@400;500;700&family=Open+Sans:ital,wght@1,400&family=Arimo:wght@400;700&display=swap" rel="stylesheet">
<style>
  :root {
    --backdrop: #2a2a2c;
    --card-top: #2d4aa0;
    --card-mid: #1f5bb0;
    --card-bottom: #1a78c4;
    --back-bottom: #0b84c9;
    --band-red: #b71d24;
    --band-red-dark: #8f151b;
    --ring-red: #b3242a;
    --cream: #efe6d2;
    --text-light: #f2f5fb;
    --pill-text: #1a2a5a;
    --pill-bg: #f4f6fa;
  }
  * { margin: 0; padding: 0; box-sizing: border-box; }
  html, body { width: 1138px; height: 1200px; overflow: hidden; background: var(--backdrop); }
  .canvas { position: relative; width: 1138px; height: 1200px; }

  .card {
    position: absolute;
    width: 377px;
    height: 620px;
    border-radius: 14px;
    overflow: hidden;
    color: var(--text-light);
    text-align: center;
  }
  .card-front {
    left: 155px; top: 276px;
    background: linear-gradient(200deg, #363f92 0%, var(--card-top) 25%, var(--card-mid) 60%, var(--card-bottom) 100%);
  }
  .card-back {
    left: 576px; top: 274px;
    background: linear-gradient(200deg, #33408f 0%, var(--card-top) 25%, var(--card-mid) 55%, var(--back-bottom) 100%);
  }

  .brand-mark {
    position: absolute;
    left: 50%;
    transform: translateX(-50%);
    border-radius: 50%;
    background: var(--cream);
    border: 7px solid var(--ring-red);
    display: flex; align-items: center; justify-content: center;
    font-family: "Ubuntu", sans-serif;
    font-weight: 700;
    color: var(--ring-red);
  }
  .card-front .brand-mark { top: 30px; width: 150px; height: 150px; font-size: 22px; }
  .card-back .brand-mark { top: 398px; width: 92px; height: 92px; font-size: 14px; border-width: 5px; }

  .holder-name {
    position: absolute; top: 196px; width: 100%;
    font-family: "Ubuntu", sans-serif; font-weight: 500; font-size: 26px;
  }
  .credentials {
    position: absolute; top: 228px; width: 100%;
    font-family: "Open Sans", sans-serif; font-style: italic; font-size: 14.5px; line-height: 21px;
  }

  .contact-divider { position: absolute; top: 310px; left: 76px; width: 225px; height: 22px; }

  .contact-list {
    position: absolute; top: 344px; width: 100%;
    font-family: "Ubuntu", sans-serif; font-size: 15.5px; line-height: 23px;
  }

  .services-band {
    position: absolute; top: 454px; left: 0; width: 100%; height: 88px;
    background: linear-gradient(180deg, var(--band-red) 0%, var(--band-red-dark) 100%);
  }
  .services-pill {
    position: absolute; top: 440px; left: 95px; width: 186px; height: 28px;
    border-radius: 14px; background: var(--pill-bg);
    border: 2px solid #c9d3e6;
    font-family: "Ubuntu", sans-serif; font-weight: 700; font-size: 17px; letter-spacing: 2.5px;
    color: var(--pill-text); line-height: 24px;
  }
  .services-text {
    position: absolute; top: 476px; width: 100%;
    font-family: "Arimo", sans-serif; font-size: 13.5px; line-height: 20px;
  }
  .mission {
    position: absolute; top: 551px; width: 100%;
    font-family: "Arimo", sans-serif; font-size: 15px; line-height: 19.5px;
  }

  .mark-pattern {
    position: absolute; inset: 0 0 150px 0;
    background: radial-gradient(ellipse at 50% 40%, rgba(90,120,200,0.18) 0%, rgba(30,70,160,0) 70%);
  }
  .back-name {
    position: absolute; top: 510px; width: 100%;
    font-family: "Arimo", sans-serif; font-weight: 700; font-size: 36px; letter-spacing: 1px;
    color: var(--text-light);
  }
  .tagline {
    position: absolute; top: 563px; width: 100%;
    font-family: "Arimo", sans-serif; font-size: 18.5px; letter-spacing: 0.3px;
  }
</style>
</head>
<body>
<main class="canvas">

  <section class="card card-front" aria-label="Business card front">
    <div class="brand-mark">Jolly Paws</div>

    <h1 class="holder-name">Rebecca Thornbury</h1>
    <p class="credentials">Qualified in Dog Behavioural Training,<br>Natural Animal Healthcare and<br>Animal Health Science</p>

    <svg class="contact-divider" viewBox="0 0 225 22" aria-hidden="true">
      <line x1="0" y1="11" x2="60" y2="11" stroke="#c2262c" stroke-width="2"/>
      <line x1="165" y1="11" x2="225" y2="11" stroke="#c2262c" stroke-width="2"/>
      <g fill="#2b4fa3" stroke="#c2262c" stroke-width="2">
        <circle cx="86" cy="11" r="9.5"/>
        <circle cx="112" cy="11" r="9.5"/>
        <circle cx="138" cy="11" r="9.5"/>
      </g>
      <path d="M81.5 8.5 q4.5 -3 9 0 l-1.2 1.6 h-1.6 l-0.6 -1.2 h-2.2 l-0.6 1.2 h-1.6 z M82.5 10.5 h7 v4 h-7 z" fill="#eef2fa"/>
      <rect x="107" y="7.5" width="10" height="7" fill="#eef2fa"/>
      <path d="M107 7.5 l5 4 l5 -4" fill="none" stroke="#2b4fa3" stroke-width="1"/>
      <g fill="none" stroke="#eef2fa" stroke-width="1">
        <circle cx="138" cy="11" r="5"/>
        <ellipse cx="138" cy="11" rx="2.2" ry="5"/>
        <line x1="133" y1="11" x2="143" y2="11"/>
      </g>
    </svg>

    <address class="contact-list" style="font-style:normal">
      0400 275 618<br>
      hello@jollypaws1.com<br>
      www.jollypaws1.com
    </address>

    <div class="services-band"></div>
    <div class="services-pill">SERVICES</div>
    <p class="services-text">Providing Individual Coaching<br>Strategies to Create Happy,<br>Healthy and Social Canine Companions</p>

    <p class="mission">Promoting communication and<br>connection between dogs &amp; their families</p>
  </section>

  <section class="card card-back" aria-label="Business card back">
    <div class="mark-pattern" role="img" aria-label="Faint repeating brand mark pattern"></div>
    <div class="brand-mark">Jolly Paws</div>
    <h2 class="back-name">JOLLY PAWS</h2>
    <p class="tagline">HAPPY DOGS, HAPPY OWNERS</p>
  </section>

</main>
</body>
</html>
```